Company identity deisgn should support 2 languages

I would like to get our company identity design
This includes the following only
Business Cards 2 languages Arabic and English
Email signature
Letterhead
Linkedin profile images
Attached is the logo in Ai format

Requirements
Must have
• For business card
Must have
Name and Adrees in arabic
Name and Address in english
You might use both side of the card
Should not have
• Any pictures other than the logo

```html
<!DOCTYPE html>
<html lang="en">
<head>
<meta charset="utf-8">
<title>Neural Grid Systems — Letterhead</title>
<link href="https://fonts.googleapis.com/css2?family=Questrial&family=Cairo:wght@400&display=swap" rel="stylesheet">
<style>
  :root {
    --brand-blue: #1479be;
    --band-grey: #6d6e70;
    --ink: #2f2f2f;
    --ink-soft: #555657;
    --paper: #ffffff;
    --sig-tone: #e6e6e6;
  }
  * { margin: 0; padding: 0; box-sizing: border-box; }
  html, body { width: 960px; height: 1200px; overflow: hidden; background: var(--paper); }
  body { font-family: "Questrial", sans-serif; color: var(--ink); }

  .letterhead { position: relative; width: 960px; height: 1200px; background: var(--paper); }

  .brand {
    position: absolute; top: 82px; left: 0; width: 960px;
    display: flex; justify-content: center; align-items: center; gap: 12px;
  }
  .brand-dot { width: 26px; height: 26px; border-radius: 50%; background: var(--brand-blue); }
  .brand-name { font-size: 30px; letter-spacing: 1px; color: var(--brand-blue); }

  .salutation { position: absolute; top: 353px; left: 88px; font-size: 21px; }

  .letter-body { position: absolute; top: 415px; left: 88px; width: 792px; }
  .letter-body p {
    font-size: 13px; line-height: 18.4px; text-align: justify; color: var(--ink);
    margin-bottom: 18.4px;
  }

  .closing { position: absolute; top: 799px; left: 88px; font-size: 13px; }
  .signature {
    position: absolute; top: 845px; left: 88px; width: 124px; height: 66px;
    background: linear-gradient(90deg, var(--paper), var(--sig-tone), var(--paper));
  }

  .contact-list { position: absolute; top: 1046px; left: 52px; list-style: none; }
  .contact-list li {
    display: flex; align-items: center; gap: 10px;
    font-size: 13.5px; line-height: 17.4px; color: var(--ink-soft);
  }
  .contact-list svg { width: 12px; height: 12px; fill: var(--brand-blue); }

  .address { position: absolute; top: 1032px; right: 56px; text-align: right; color: var(--ink-soft); }
  .address-ar { font-family: "Cairo", sans-serif; font-size: 13px; line-height: 22px; direction: rtl; }
  .address-en { margin-top: 8px; font-size: 13.5px; line-height: 17.4px; }

  .footer-band { position: absolute; top: 1142px; left: 0; width: 960px; height: 28px; }
  .footer-band svg { position: absolute; inset: 0; }
  .site-url {
    position: absolute; top: 1149px; left: 44px;
    font-size: 13px; letter-spacing: 3px; color: var(--paper);
  }
</style>
</head>
<body>
<main class="letterhead">
  <header class="brand">
    <span class="brand-dot"></span>
    <span class="brand-name">NEURAL GRID SYSTEMS</span>
  </header>

  <h1 class="salutation" style="font-weight:400">Dear Mr. Carter,</h1>

  <section class="letter-body">
    <p>Lorem ipsum dolor sit amet, consectetur adipiscing elit. Donec orci purus, luctus vitae dignissim eu, iaculis sed purus. Vivamus faucibus, ipsum nec aliquet viverra, leo mauris condimentum ligula, sit amet sagittis enim ligula quis arcu. Nam egestas tortor id nisi porttitor mattis. In tortor ante, ultricies in suscipit a, tempus non massa. Vivamus et auctor mi. Fusce vel massa nulla. Phasellus nec eros mauris, et scelerisque orci.</p>
    <p>Donec malesuada orci vitae nulla accumsan porta a id massa. Quisque accumsan iaculis magna sit amet fringilla. Maecenas consequat, magna eget tincidunt semper, odio nibh rutrum mi, id feugiat ante nisi eu risus. Vestibulum nunc orci, rhoncus a placerat in, ultricies in mi. Cras mattis varius eros, vel fringilla nisi suscipit eget. Quisque scelerisque sagittis nulla at porttitor.</p>
    <p>Sed id augue vitae urna euismod commodo aliquet a quam. Pellentesque arcu velit, cursus et malesuada ut, consequat et diam. Nullam erat sem, rhoncus id ullamcorper vitae, rhoncus et arcu. In ultricies ultricies nulla, ut rutrum nisi iaculis at. Donec eu magna a metus ornare faucibus. Fusce aliquet faucibus ultricies. Morbi semper, est id tincidunt gravida, sem arcu adipiscing lacus, ac bibendum nulla leo eu purus. Quisque nec diam sed risus consectetur a ccumsan quis quis nibh. Vestibulum id purus lorem.</p>
    <p>It is a long established fact that a reader will be distracted by the readable content of a page when looking at its layout. The point of using Lorem Ipsum is that it has a more-or-less normal distribution of letters, as opposed to using 'Content here, content here', making it look like readable English. Many desktop publishing packages</p>
  </section>

  <p class="closing">Sincerely,</p>
  <div class="signature" role="img" aria-label="Handwritten signature of the sender"></div>

  <ul class="contact-list">
    <li><svg viewBox="0 0 24 24"><path d="M6.6 10.8a15.2 15.2 0 0 0 6.6 6.6l2.2-2.2c.3-.3.7-.4 1-.2 1.1.4 2.3.6 3.6.6.6 0 1 .4 1 1V20c0 .6-.4 1-1 1A17 17 0 0 1 3 4c0-.6.4-1 1-1h3.5c.6 0 1 .4 1 1 0 1.3.2 2.5.6 3.6.1.3 0 .7-.2 1z"/></svg>555-214-7730</li>
    <li><svg viewBox="0 0 24 24"><path d="M7 1h10a2 2 0 0 1 2 2v18a2 2 0 0 1-2 2H7a2 2 0 0 1-2-2V3a2 2 0 0 1 2-2zm0 3v14h10V4z"/></svg>555-618-2094</li>
    <li><svg viewBox="0 0 24 24"><path d="M6 2h12v6H6zM3 9h18a1 1 0 0 1 1 1v8h-4v4H6v-4H2v-8a1 1 0 0 1 1-1zm5 7v4h8v-4z"/></svg>555-309-4416</li>
    <li><svg viewBox="0 0 24 24"><path d="M2 5h20v14H2zm2 2v.5l8 5 8-5V7z"/></svg>info@neuralgridsystems.com</li>
  </ul>

  <address class="address" style="font-style:normal">
    <div class="address-ar">4120 طريق سيدار هولو<br>جونو، ألاسكا 99801</div>
    <div class="address-en">4120 Cedar Hollow Road<br>Juneau, Alaska 99801</div>
  </address>

  <div class="footer-band">
    <svg viewBox="0 0 960 28" preserveAspectRatio="none" aria-hidden="true">
      <rect x="0" y="0" width="960" height="28" fill="var(--brand-blue)"/>
      <polygon points="752,0 960,0 960,28 738,28" fill="var(--band-grey)"/>
    </svg>
  </div>
  <span class="site-url">WWW.NEURALGRIDSYSTEMS.COM</span>
</main>
</body>
</html>
```